Neon Lodging Offers Website looking for new design

We are a online travel discounter based around hotel accommodations in Las Vegas. We need a wordpress design that will be used as our corporate cover page, and also for the affiliate pages. The current design can be viewed at http://postweaveforum.com/clients/neonoffer/ and the final design needs to include most of the navigation components. The affiliate pages will need a space to display the booking engine, for example, as shown at http://www.qrv.travel/marcoti. Our general color scheme is red/black, and the two logos we use are attached.

Because this is a crowded niche it is extremely important that we set ourselves apart in the design. The more visually stunning and out of the box the design, the better. The site needs to look distinctively different than anything else online. Since the overall layout is very basic and does not have to provide a lot of information, it leaves a lot of flexibility in design concepts.

We realize it is a truncated timetable, which is why the increased fee for your time and guaranteed payout.

Industry/Entity Type

Travel

```html
<!DOCTYPE html>
<html lang="en">
<head>
<meta charset="utf-8">
<title>Neon Lodging Offers</title>
<link href="https://fonts.googleapis.com/css2?family=Raleway:wght@400;500;600&family=Open+Sans:wght@400;600&display=swap" rel="stylesheet">
<style>
:root{
  --red:#d0111b;
  --red-dark:#a80a12;
  --ink:#222;
  --grey-band:#e9e9e9;
  --footer:#2b2b2b;
  --footer-bottom:#222;
  --muted:#666;
  --line:#dcdcdc;
  --white:#fff;
}
*{box-sizing:border-box;margin:0;padding:0}
html,body{width:696px;height:1200px;overflow:hidden;background:var(--white)}
body{position:relative;font-family:"Open Sans",sans-serif;color:var(--ink)}
.abs{position:absolute}

/* hero */
.hero{left:0;top:0;width:696px;height:358px;background:linear-gradient(160deg,#c9a56c 0%,#b98a4c 40%,#8f5f2c 75%,#6e4220 100%)}
.hero-photo{left:0;top:0;width:696px;height:358px;background:radial-gradient(ellipse at 65% 30%,rgba(255,240,200,.55),transparent 60%),linear-gradient(180deg,rgba(0,0,0,0) 60%,rgba(70,40,15,.35))}
.nav-band{left:0;top:36px;width:696px;height:24px;background:rgba(255,255,255,.25)}
.nav a{position:absolute;top:43px;font-family:"Raleway",sans-serif;font-weight:600;font-size:8.5px;color:#111;text-decoration:none;letter-spacing:.2px}
.nav .sep{position:absolute;top:45px;width:5px;height:5px;background:#111;transform:rotate(45deg)}
.brand{left:278px;top:14px;width:120px;text-align:center}
.brand-dot{display:block;margin:0 auto 6px;width:42px;height:42px;border-radius:50%;background:var(--red)}
.brand-name{font-family:"Raleway",sans-serif;font-weight:500;font-size:10px;color:var(--red)}

.search{left:106px;top:116px;width:159px;height:192px;background:var(--red);color:var(--white);font-family:"Raleway",sans-serif}
.search-head{height:28px;background:var(--red-dark);font-size:12.5px;padding:7px 0 0 14px}
.search label{position:absolute;font-size:7px;color:#ffe5e5}
.search .field{position:absolute;height:15px;background:var(--white);border:1px solid #e6e6e6;font-family:"Open Sans",sans-serif;font-size:5.5px;color:#555;padding:4px 0 0 5px}
.cal{position:absolute;right:3px;top:3px;width:8px;height:7px;border:1px solid #888}
.search-btn{position:absolute;left:13px;top:165px;width:62px;height:16px;background:#111;color:var(--white);font-size:7.5px;text-align:center;padding-top:3px}
.dots{left:326px;top:339px;display:flex;gap:3px}
.dots i{width:8px;height:8px;border-radius:50%;background:var(--white);display:block}

/* about */
.about-title{left:0;top:378px;width:696px;text-align:center;font-family:"Raleway",sans-serif;font-size:17px;font-weight:400}
.about-text{left:118px;top:404px;width:460px;text-align:center;font-size:5.4px;line-height:9px;color:var(--muted)}
.about-text p+p{margin-top:5px}
.feature{width:160px;text-align:center}
.feature .photo{width:122px;height:122px;border-radius:50%;margin:0 auto;box-shadow:0 4px 4px -2px rgba(0,0,0,.25)}
.feature h3{margin-top:15px;font-family:"Raleway",sans-serif;font-weight:500;font-size:11.5px;color:var(--red)}
.feature p{margin-top:3px;font-size:5.4px;line-height:9px;color:var(--muted)}

/* packages */
.packages{left:0;top:676px;width:696px;height:246px;background:var(--grey-band)}
.pk-tab{left:264px;top:676px;width:160px;height:31px}
.pk-title{left:264px;top:683px;width:160px;text-align:center;font-family:"Raleway",sans-serif;font-size:14px}
.card{top:723px;width:120px;height:167px;background:var(--white);border:1px solid #d5d5d5}
.card-head{position:absolute;left:-1px;top:-1px;width:120px;height:33px}
.card-head span{position:absolute;left:0;top:8px;width:100%;text-align:center;font-family:"Raleway",sans-serif;font-size:13px;color:var(--white)}
.card ul{list-style:none;position:absolute;left:10px;top:48px;width:98px}
.card li{font-size:6.2px;text-align:center;height:18px;padding-top:3px;border-bottom:1px solid var(--line)}
.card li:last-child{border-bottom:none}
.price{position:absolute;left:0;top:112px;width:100%;text-align:center;font-size:17px}
.price small{font-size:10px}
.buy{position:absolute;left:12px;top:139px;width:96px;height:19px;background:linear-gradient(#2a2a2a,#0d0d0d);color:var(--white);font-size:7.5px;text-align:center;padding-top:4px}

/* help form */
.help{left:0;top:922px;width:696px;height:125px;background:linear-gradient(90deg,#a50a12,#d3121c 30%,#d3121c 70%,#a50a12)}
.help-title{left:0;top:943px;width:696px;text-align:center;font-family:"Raleway",sans-serif;font-size:13.5px;color:var(--white)}
.input{height:16px;background:linear-gradient(#fff,#ececec);border:1px solid #ddd;font-size:5.5px;color:#666;padding:4px 0 0 6px}
.submit{left:310px;top:1013px;width:55px;height:17px;border:1px solid var(--white);border-radius:2px;color:var(--white);font-size:7.5px;font-weight:600;text-align:center;padding-top:3px}

/* footer */
.footer{left:0;top:1047px;width:696px;height:123px;background:var(--footer)}
.fcol{top:1068px;color:#ddd}
.fcol h4{font-family:"Raleway",sans-serif;font-weight:400;font-size:9.5px;margin-bottom:6px}
.fcol p{font-size:6px;line-height:11.2px;color:#bbb}
.social{display:flex;gap:3px;margin-top:4px}
.social i{display:block;width:11px;height:11px;background:#e8e8e8;border-radius:2px}
.footbar{left:0;top:1170px;width:696px;height:30px;background:var(--footer-bottom)}
.copy{left:104px;top:1182px;font-size:5px;color:#999}
</style>
</head>
<body>

<section class="abs hero" role="img" aria-label="Warm-lit hotel bedroom with bed, lamps, sofa and shuttered windows"></section>
<div class="abs hero-photo"></div>
<div class="abs nav-band"></div>
<nav class="nav">
  <a style="left:145px">HOME</a><span class="sep" style="left:187px"></span>
  <a style="left:213px">GROUPS</a>
  <a style="left:413px">SEARCH EVENTS</a><span class="sep" style="left:498px"></span>
  <a style="left:522px">CONTACT US</a>
</nav>
<div class="abs brand"><span class="brand-dot"></span><span class="brand-name">neonoffers.travel</span></div>

<form class="abs search">
  <div class="search-head">Find Your Hotel Now</div>
  <label style="left:12px;top:35px">Location</label>
  <div class="field" style="left:12px;top:45px;width:135px">Please type city name</div>
  <label style="left:12px;top:70px">Check-In</label>
  <label style="left:80px;top:70px">Check-Out</label>
  <div class="field" style="left:12px;top:80px;width:66px">02/20/15<span class="cal"></span></div>
  <div class="field" style="left:80px;top:80px;width:67px">02/03/15<span class="cal"></span></div>
  <label style="left:12px;top:103px">Adults</label>
  <label style="left:82px;top:103px">Childrens</label>
  <div class="field" style="left:12px;top:113px;width:66px">02</div>
  <div class="field" style="left:81px;top:113px;width:66px">02</div>
  <label style="left:12px;top:134px">Resident</label>
  <div class="field" style="left:12px;top:144px;width:135px">Indian</div>
  <div class="search-btn">Search Now</div>
</form>
<div class="abs dots"><i></i><i></i><i></i><i></i></div>

<h1 class="abs about-title">About Neon Lodging Offers Mainpage</h1>
<div class="abs about-text">
  <p>Vivamus porttitor purus nisi eleifend libero a tempus libero lectus feugiat felis Morbi diam mauris viverra in gravida eu mattis in ante Morbi eget arcu Morbi porta libero id ullamcorper nonummy nibh ligula pulvinar metus eget consectetuer augue nisi quis lacus Ut ac mi quis lacus mollis aliquam Curabitur iaculis tempus eros Curabitur vel mi sit amet magna malesuada ultrices Ut nisi erat fermentum vel congue id euismod in elit Fusce ultrices orci ac feugiat suscipit leo massa</p>
  <p>Mauris vel lacus vitae felis vestibulum volutpat Etiam est nunc venenatis in tristique eu imperdiet ac nisl Cum sociis natoque penatibus et magnis dis p</p>
</div>

<div class="abs feature" style="left:122px;top:481px">
  <div class="photo" role="img" aria-label="Hotel suite with bed and television" style="background:linear-gradient(150deg,#c98a4a,#8a4e25 60%,#e9ddd0)"></div>
  <h3>Watch Gallery</h3>
  <p>Ectetuer augue nisi quis lacus Ut ac mi quis<br>lacus mollis aliquam Curabitur</p>
</div>
<div class="abs feature" style="left:273px;top:481px">
  <div class="photo" role="img" aria-label="Hotel bedroom with framed pictures and red bench" style="background:linear-gradient(160deg,#b97844,#7a3b1e 55%,#a8141a)"></div>
  <h3>Why Choose Us</h3>
  <p>Ectetuer augue nisi quis lacus Ut ac mi quis<br>lacus mollis aliquam Curabitur</p>
</div>
<div class="abs feature" style="left:424px;top:481px">
  <div class="photo" role="img" aria-label="Guest booking a stay on a laptop" style="background:linear-gradient(150deg,#d9b58a,#b58157 55%,#efe9e2)"></div>
  <h3>Book Now</h3>
  <p>Ectetuer augue nisi quis lacus Ut ac mi quis<br>lacus mollis aliquam Curabitur</p>
</div>

<section class="abs packages"></section>
<svg class="abs pk-tab" viewBox="0 0 160 31"><path d="M0 0 H160 L148 31 H12 Z" fill="#d4d4d4"/></svg>
<h2 class="abs pk-title">Our Packages</h2>

<div class="abs card" style="left:105px">
  <svg class="card-head" viewBox="0 0 120 33" preserveAspectRatio="none"><path d="M0 0 H120 V28 Q60 36 0 28 Z" fill="#d0111b"/></svg><div class="card-head"><span>Package 1</span></div>
  <ul><li>Calm Surroundings</li><li>Clean Rooms</li><li>Hotel Bus</li></ul>
  <div class="price"><small>$</small>200</div><div class="buy">BUY NOW</div>
</div>
<div class="abs card" style="left:227px">
  <svg class="card-head" viewBox="0 0 120 33" preserveAspectRatio="none"><path d="M0 0 H120 V28 Q60 36 0 28 Z" fill="#d0111b"/></svg><div class="card-head"><span>Package 2</span></div>
  <ul><li>Calm Surroundings</li><li>Clean Rooms</li><li>Hotel Bus</li></ul>
  <div class="price"><small>$</small>300</div><div class="buy">BUY NOW</div>
</div>
<div class="abs card" style="left:349px">
  <svg class="card-head" viewBox="0 0 120 33" preserveAspectRatio="none"><path d="M0 0 H120 V28 Q60 36 0 28 Z" fill="#d0111b"/></svg><div class="card-head"><span>Package 3</span></div>
  <ul><li>Calm Surroundings</li><li>Clean Rooms</li><li>Hotel Bus</li></ul>
  <div class="price"><small>$</small>400</div><div class="buy">BUY NOW</div>
</div>
<div class="abs card" style="left:471px">
  <svg class="card-head" viewBox="0 0 120 33" preserveAspectRatio="none"><path d="M0 0 H120 V28 Q60 36 0 28 Z" fill="#d0111b"/></svg><div class="card-head"><span>Package 4</span></div>
  <ul><li>Calm Surroundings</li><li>Clean Rooms</li><li>Hotel Bus</li></ul>
  <div class="price"><small>$</small>500</div><div class="buy">BUY NOW</div>
</div>

<section class="abs help" role="img" aria-label="Red-toned hotel room backdrop"></section>
<h2 class="abs help-title">Need a Help Please fill our Form</h2>
<div class="abs input" style="left:151px;top:970px;width:121px">First Name</div>
<div class="abs input" style="left:276px;top:970px;width:121px">Last Name</div>
<div class="abs input" style="left:151px;top:990px;width:121px">Email address</div>
<div class="abs input" style="left:276px;top:990px;width:121px">Phone no.</div>
<div class="abs input" style="left:401px;top:970px;width:122px;height:36px">Message</div>
<div class="abs submit">Submit</div>

<footer class="abs footer"></footer>
<div class="abs fcol" style="left:104px"><h4>Company</h4><p>Home<br>About Us<br>Why Choose Us<br>Services Provide<br>Contact Us</p></div>
<div class="abs fcol" style="left:204px"><h4>Resources</h4><p>Search Events<br>Our Packages<br>Need a Help<br>Testimonials</p></div>
<div class="abs fcol" style="left:302px"><h4>Support</h4><p>Privacy Policy<br>Term of Use<br>Help<br>Support</p></div>
<div class="abs fcol" style="left:394px"><h4>Contact Info</h4><p>Name: Dana R. Whitfield<br>Email: dana.whitfield@neonoffers.travel<br>Phone: 555-214-730</p>
  <div class="social"><i></i><i></i><i></i></div></div>
<div class="abs footbar"></div>
<div class="abs copy">© 2015 Company Name &nbsp;All right reserved &nbsp;Term of Use</div>

</body>
</html>
```